依頼詳細
2ヶ月集中プランというサービスを売り出しており、チラシのポスティングを行って集客をしています。
今回は、現在使用しているチラシには満足していますが、別のパターンのチラシをデザインしていただきたく思っております。
現在アプローチできていない層にひっかかるデザインを希望しています。
必ず入れてほしい情報はこちらです
・店舗ウェブサイトのQRコード
・他プランの紹介
・店舗情報
・プランの詳細

データはこちらにあるものをご自由に使ってください
https://files.kumoshare-example.net/folders/7hTqLm2pXw9RzK4vNc8sYdJ3bFgA1eUo?usp=sharing

2ヶ月集中プランについてのページです
https://velnakai-example.com/special/2month/

サラダ定額制というサービスの詳細はこちらです
https://velnakai-example.com/special/salad/

記載項目
社名:Velna&Partners株式会社
URL:https://velnakai-example.com/
サイズ
A4
ページ数
両面
希望イメージ
シンプル 複雑
単色 カラフル
暗い 明るい
日常 高級
遊び心 厳粛
未来的 伝統的
女性的 男性的
希望する色
納品ファイル
• 高解像度JPG (.jpg)
• イラストレーター形式 (.ai)
補足説明

見た瞬間、まさに求めてるデザインだと確信しました。素晴らしいの一言です。しっかり内容を把握いただいて作成されているのが伝わります。

この度は多くのご提案をいただき、誠にありがとうございました!
また次回機会があればよろしくお願いします。

```html
<!DOCTYPE html>
<html lang="ja">
<head>
<meta charset="utf-8">
<title>VELNA TOKYO 2ヶ月短期集中プラン</title>
<link href="https://fonts.googleapis.com/css2?family=Noto+Sans+JP:wght@400;500;700;900&display=swap" rel="stylesheet">
<style>
  :root{
    --pink:#e8628f;
    --pink-deep:#d94a7c;
    --pink-soft:#f6c9d8;
    --pink-pale:#fde8ef;
    --ink:#2a2a2a;
    --charcoal:#4a4a4c;
    --white:#ffffff;
    --photo-skin:#e9d6cc;
    --photo-wall:#f1ece8;
  }
  *{margin:0;padding:0;box-sizing:border-box}
  html,body{width:846px;height:1200px;overflow:hidden;background:var(--white)}
  body{font-family:"Noto Sans JP",sans-serif;color:var(--ink)}
  .flyer{position:relative;width:846px;height:1200px;overflow:hidden;background:var(--white)}

  .hero-photo{position:absolute;right:0;top:0;width:400px;height:690px;
    background:linear-gradient(160deg,var(--photo-wall) 0%,var(--photo-skin) 55%,#d7bfb3 100%)}
  .brand{position:absolute;left:55px;top:26px;text-align:center;color:var(--ink);font-weight:700}
  .brand-name{font-size:50px;letter-spacing:10px;line-height:1}
  .brand-city{font-size:14px;letter-spacing:6px;margin-top:4px}

  .tagline{position:absolute;left:70px;top:140px;display:flex;align-items:center;gap:10px;font-weight:900;font-size:30px;color:var(--pink-deep)}
  .tag-pill{background:var(--white);border:3px solid var(--pink);border-radius:30px;padding:4px 22px;transform:skewX(-8deg)}
  .tag-x{font-size:34px;color:var(--pink)}

  .headline{position:absolute;left:70px;top:215px;color:var(--pink-deep);font-weight:900;line-height:1.1}
  .headline-lead{font-size:26px;vertical-align:middle;margin-right:6px;display:inline-block}
  .headline-big{font-size:86px}
  .headline-line2{font-size:70px;display:block}

  .features{position:absolute;left:70px;top:430px;display:flex;gap:14px;list-style:none}
  .feature{width:128px;height:128px;border-radius:50%;background:var(--pink);color:var(--white);
    display:flex;align-items:center;justify-content:center;text-align:center;font-weight:700;font-size:16px;line-height:1.35}
  .feature small{display:block;font-size:11px;font-weight:500}

  .salad-photo{position:absolute;left:0;top:590px;width:430px;height:340px;border-radius:0 0 200px 0;
    background:radial-gradient(circle at 45% 55%,#b34a3c 0%,#7a9a4a 40%,#cfd9b4 75%,#eef1e4 100%)}
  .training-photo{position:absolute;right:0;top:690px;width:430px;height:310px;
    background:linear-gradient(120deg,#9a8f88 0%,#d8c9c1 50%,#4a4446 100%)}

  .points{position:absolute;left:40px;top:725px;font-weight:900;font-size:23px;line-height:1.75;color:var(--pink-deep)}
  .points span{background:var(--white);padding:2px 8px;box-decoration-break:clone}

  .plan{position:absolute;left:0;top:1000px;width:846px;height:117px;background:var(--charcoal);color:var(--white);padding:10px 40px 0}
  .plan-lead{font-size:15px;font-weight:700;line-height:1.3}
  .plan-row{display:flex;align-items:center;gap:20px;margin-top:2px;line-height:1.2}
  .plan-name{font-size:34px;font-weight:900}
  .plan-price{font-size:34px;font-weight:900;color:var(--pink-soft)}
  .plan-price em{font-style:normal;font-size:20px}
  .plan-note{font-size:10px;line-height:1.4}
  .plan-items{display:flex;gap:10px;margin-top:4px}
  .plan-item{background:var(--white);color:var(--charcoal);font-size:13px;font-weight:700;line-height:1.4;padding:2px 12px}

  .cta{position:absolute;left:0;top:1117px;width:846px;height:83px;background:var(--pink);color:var(--white);text-align:center;padding-top:10px}
  .cta-main{font-size:29px;font-weight:900;letter-spacing:1px;line-height:1.4}
  .cta-sub{font-size:14px;font-weight:500;margin-top:2px}
</style>
</head>
<body>
<main class="flyer">
  <div class="hero-photo" role="img" aria-label="笑顔でストレッチするトレーニングウェアの女性の写真"></div>

  <div class="brand">
    <div class="brand-name">VELNA</div>
    <div class="brand-city">-TOKYO-</div>
  </div>

  <div class="tagline">
    <span class="tag-pill">トレーニング</span><span class="tag-x">×</span><span class="tag-pill">ジム飯</span><span>で</span>
  </div>

  <h1 class="headline">
    <span class="headline-lead">たった</span><span class="headline-big">2ヶ月で</span>
    <span class="headline-line2">カラダ変わる!</span>
  </h1>

  <ul class="features">
    <li class="feature"><div><small>実力のある<br>トレーナーによる</small>パーソナル<br>トレーニング</div></li>
    <li class="feature"><div>トレーニング<br>ルーム<br>通い放題</div></li>
    <li class="feature"><div>おいしくて<br>ヘルシーな<br>食事付き</div></li>
  </ul>

  <div class="salad-photo" role="img" aria-label="彩り豊かなサラダボウルの写真"></div>
  <div class="training-photo" role="img" aria-label="女性トレーナーと一緒にトレーニングする様子の写真"></div>

  <p class="points">
    <span>手ぶらで通える</span><br>
    <span>トレーナー・スタッフ全員女性</span><br>
    <span>食事指導とジム飯で食生活もサポート</span>
  </p>

  <section class="plan">
    <div class="plan-lead">トレーニングと食事で結果を出す</div>
    <div class="plan-row">
      <div class="plan-name">2ヶ月短期集中プラン</div>
      <div class="plan-price">198,000<em>円</em></div>
      <div class="plan-note">税込価格/入会金11,000円が別途必要<br>サラダ定額なしの場合は165,000円</div>
    </div>
    <div class="plan-items">
      <span class="plan-item">パーソナルトレーニング60分×16回/2ヶ月</span>
      <span class="plan-item">サラダ定額制</span>
      <span class="plan-item">トレーニングルーム通い放題</span>
    </div>
  </section>

  <footer class="cta">
    <div class="cta-main">体験トレーニングも実施中!お気軽にご予約ください。</div>
    <div class="cta-sub">詳しい内容や他のプラン、ご予約等は裏面をご覧ください。</div>
  </footer>
</main>
</body>
</html>
```